Morrow Family Reunion Flyer

A flyer detailing family reunion events. It should be complimentary to the logo style and fonts. BE DIFFERENT AVOID TEMPLATES

The 2015 Morrow Family Reunion
Descendants of Tobias Elwin Harold Morrow

Friday August 14th 2pm
Jummah Prayer At Sunvale Mosque
Followed by Family Get Together

Saturday august 15th 12pm
Family Reunion Picnic
4123 morrow Dr.
fairlen

Hosted by the Children of The Prestigious Morrow Family

Colors
0355a3
9bcb3c

Requirements
Must have
• Logo

```html
<!DOCTYPE html>
<html lang="en">
<head>
<meta charset="utf-8">
<title>Morrow Family Reunion 2015</title>
<link href="https://fonts.googleapis.com/css2?family=Quicksand:wght@700&family=Open+Sans:wght@700&display=swap" rel="stylesheet">
<style>
  :root {
    --green: #17803f;
    --blue: #2b9ad6;
    --ink: #161616;
    --outline: #123a5c;
    --faint: #d3e9da;
    --frame: #333333;
    --paper: #ffffff;
  }
  html, body {
    margin: 0;
    padding: 0;
    width: 1200px;
    height: 1000px;
    overflow: hidden;
    background: var(--paper);
  }
  .canvas {
    position: relative;
    width: 1200px;
    height: 1000px;
    background: var(--paper);
  }
  .flyer {
    position: absolute;
    left: 255px;
    top: 12px;
    width: 690px;
    height: 976px;
    border: 1px solid var(--frame);
    box-sizing: border-box;
    background: var(--paper);
    overflow: hidden;
  }
  .backdrop-rings {
    position: absolute;
    left: 0;
    top: 0;
  }
  .logo {
    position: absolute;
    left: 220px;
    top: 18px;
    width: 250px;
    height: 250px;
  }
  .logo-name {
    position: absolute;
    left: 0;
    top: 0;
    width: 250px;
    height: 250px;
    display: flex;
    align-items: center;
    justify-content: center;
    text-align: center;
    font-family: "Quicksand", sans-serif;
    font-weight: 700;
    font-size: 30px;
    line-height: 1.1;
    color: var(--green);
  }
  .line {
    position: absolute;
    left: 0;
    width: 100%;
    margin: 0;
    text-align: center;
    white-space: nowrap;
  }
  .title {
    top: 281px;
    left: 4px;
    font-family: "Quicksand", sans-serif;
    font-weight: 700;
    font-size: 45px;
    letter-spacing: 0.5px;
  }
  .title .green { color: var(--green); }
  .title .blue { color: var(--blue); }
  .detail {
    font-family: "Open Sans", sans-serif;
    font-weight: 700;
    font-size: 31.5px;
    color: var(--ink);
    left: -8px;
  }
  .date {
    font-family: "Open Sans", sans-serif;
    font-weight: 700;
    font-size: 41px;
    color: var(--blue);
    -webkit-text-stroke: 1px var(--outline);
    left: -6px;
  }
</style>
</head>
<body>
<div class="canvas">
  <main class="flyer">
    <svg class="backdrop-rings" width="690" height="976" viewBox="0 0 690 976" aria-hidden="true">
      <circle cx="345" cy="330" r="322" fill="none" stroke="var(--faint)" stroke-width="13"/>
      <circle cx="345" cy="680" r="292" fill="none" stroke="var(--faint)" stroke-width="13"/>
      <circle cx="345" cy="680" r="222" fill="none" stroke="var(--faint)" stroke-width="9"/>
    </svg>

    <div class="logo">
      <svg width="250" height="250" viewBox="0 0 250 250" aria-hidden="true">
        <circle cx="125" cy="125" r="120" fill="var(--paper)" stroke="var(--green)" stroke-width="8"/>
      </svg>
      <div class="logo-name">Morrow<br>Family</div>
    </div>

    <h1 class="line title"><span class="green">Morrow</span> <span class="blue">Family</span> <span class="green">Reunion</span> <span class="blue">2015</span></h1>

    <p class="line detail" style="top:361px;">The 2015 Morrow Family Reunion</p>
    <p class="line detail" style="top:404px;">Descendants of</p>
    <p class="line detail" style="top:452px;">Tobias Elwin Harold Morrow</p>

    <p class="line date" style="top:506px;">Friday August 14th 2pm</p>
    <p class="line detail" style="top:563px;">Jummah Prayer At Sunvale Mosque</p>
    <p class="line detail" style="top:608px;">Followed by Family Get Together</p>

    <p class="line date" style="top:655px;">Saturday august 15th 12pm</p>
    <p class="line detail" style="top:712px;">Family Reunion Picnic</p>
    <p class="line detail" style="top:761px;">4123 morrow Dr.fairlen</p>

    <p class="line detail" style="top:851px;">Hosted by the Children of</p>
    <p class="line detail" style="top:898px;">The Prestigious Morrow Family</p>
  </main>
</div>
</body>
</html>
```